Corvelle Matchmaking - Innovative AI-based Online Dating App

Hello, I am creating a new online dating app that subsumes the personalization and compatibility analysis of human matchmaking, but is combined with the convenience of modern dating apps such as brisket. The app is called Corvelle.

There is a lot of pain and fatigue in modern online dating. Corvelle uses a concise but effective questionnaire that is combined with cutting-edge AI, social psychology research, and psycholinguistic modelling to effectively and conveniently find dating matches with real compatibility - as opposed to any major app on the market. A personalized introduction for every user is generated everyday to introduce you to a new potential match - this introduction is totally unique and will never be seen before or again. The introduction is intertwined with the user’s images to create an attractive “newsletter” feel.

"Corvelle" is Italian for lagoon, which is "a shallow body of water protected from a larger body of water (usually the ocean) by sandbars, barrier islands, or coral reefs." Lagoons are beautiful, tropical, lush watery paradises - as I see it. This is meant to be the inspiration for the feel, color scheme and design of the app.

To that end, I have included concept images of lagoons to evoke the feeling of a paradise getaway where one may meet their soulmate. This is the feeling I would like to convey with the minimalist app design this product needs to compete.

I have included screenshots of the current app UI. There is a screen for
1) potential matches and incoming likes (just like Brisket) with a logo at the top. There are “Like”, “Dislike”, “Super Like”, and “Super Dislike” buttons that float over the screen as it scrolls. These button shape/colors likely need to change to match the rest of the design
2) Overview of message threads with each match
3) View of message threads
4) Settings page

I would like
1) the logo/header image to be redone (as well as the like/dislike/super like/super dislike buttons to be redone to match the new design)
2) icons for the 4 pages in the bottom navigation bar to be redone
3) color scheme to be optimized and evoking of the desired paradise but professional feeling of a hyper-intelligent (but also empathetic) matchmaker
4) design for the settings screen (to look professional and competitive with other dating apps)

The color scheme /layout/spacing/font(s) for the bubbles on the screen where new potential matches are introduced is the most important part of the design I’m looking for. It’s currently a stack of rounded rectangles basically, but I’m open to all ideas to make this app look as professional as possible while conveying the desired elegance, empathy, and uniqueness of the brand.

Thank you!

Target Market(s)

Single men and women ages 20 - 45

Industry/Entity Type

Online dating / Matchmaking

Requirements
Must have
• For the main screen where new users are being introduced (i.e. the "swipe" page on most dating apps) - some amount of matchmaking introductory text MUST be shown above the user's first profile picture, as indicated in the current screenshots.
Nice to have
• Re-designs of the top "Corvelle" logo/emblem would be nice. If changing the logo, some emblem or graphic in addition to just the text of "Corvelle" would be nice. (Like the way "plumway" has its red flame emblem)
Should not have
• The main "swipe" page should not look identical to other dating apps in the sense of being >90% just a user's first dating profile image. The competitive edge to this app is the user-to-user specific matchmaking introductory text, so some of that must be visible before a user scrolls down for further profile information.

```html
<!DOCTYPE html>
<html lang="en">
<head>
<meta charset="utf-8">
<title>Corvelle – App Screens</title>
<link rel="stylesheet" href="https://fonts.googleapis.com/css2?family=Inter:wght@400;600&family=Mulish:wght@400;600;700;800&display=swap">
<style>
  :root {
    --ink: #0c0f1a;
    --stage: #000000;
    --screen-bg: #eef3fc;
    --card: #ffffff;
    --cyan: #00c8e6;
    --azure: #0a8df0;
    --blue: #1572f0;
    --brand: #0aa8e0;
    --muted: #6b7280;
    --red: #e5262b;
    --online: #4cd964;
    --line: #e3e8f2;
    --key-bed: #d2d5db;
    --key: #fbfbfc;
    --key-dark: #aeb3bd;
  }
  * { box-sizing: border-box; margin: 0; padding: 0; }
  html, body { width: 1200px; height: 837px; overflow: hidden; }
  body {
    background: var(--stage);
    position: relative;
    font-family: "Mulish", sans-serif;
    color: var(--ink);
  }

  /* Brand header */
  .brand-mark {
    position: absolute; left: 0; right: 0; top: 76px;
    display: flex; justify-content: center; align-items: center; gap: 16px;
  }
  .brand-mark__name {
    font-family: "Mulish", sans-serif; font-weight: 600;
    font-size: 58px; letter-spacing: 3px; color: var(--brand); line-height: 1;
  }
  .brand-mark__dot { width: 62px; height: 62px; border-radius: 50%; background: var(--brand); }

  /* Screens */
  .screen {
    position: absolute; width: 216px;
    background: var(--screen-bg); border-radius: 24px; overflow: hidden;
  }
  .screen--intro { left: 90px; top: 246px; height: 466px; }
  .screen--profile { left: 350px; top: 244px; height: 468px; }
  .screen--inbox { left: 616px; top: 239px; height: 480px; background: #f0f5fd; }
  .screen--chat { left: 887px; top: 238px; height: 481px; }

  .status {
    position: absolute; left: 12px; right: 12px; top: 9px; height: 12px;
    display: flex; justify-content: space-between; align-items: center;
    font-family: "Inter", sans-serif; font-size: 6.8px; color: #333;
  }
  .status__icons { display: flex; gap: 4px; align-items: center; }

  .abs { position: absolute; }

  .app-logo {
    position: absolute; left: 0; right: 0; top: 34px;
    display: flex; justify-content: center; align-items: center; gap: 5px;
  }
  .app-logo__name { font-weight: 600; font-size: 19px; letter-spacing: 0.6px; color: var(--brand); line-height: 1; }
  .app-logo__dot { width: 19px; height: 19px; border-radius: 50%; background: var(--brand); }

  .intro-card {
    position: absolute; background: var(--card); border-radius: 14px;
    border-bottom: 1.5px solid var(--cyan);
    font-family: "Inter", sans-serif; font-size: 8.3px; line-height: 10px; color: #111;
  }
  .intro-card--letter { left: 8px; top: 70px; width: 197px; height: 143px; padding: 12px 14px 0 17px; }
  .intro-card--letter .greeting { margin-bottom: 10px; }
  .intro-card--letter strong { font-weight: 600; }

  .photo-frame {
    position: absolute; left: 9px; top: 225px; width: 196px; height: 190px;
    border: 2px solid var(--azure); border-radius: 13px;
    background: radial-gradient(ellipse at 45% 45%, #6b5247 0%, #3b3434 40%, #1c1c22 80%),
                linear-gradient(160deg, #8a6f72, #2a2b35);
    background-blend-mode: multiply;
  }

  .action {
    position: absolute; border-radius: 50%; display: flex; align-items: center; justify-content: center;
    transform: translate(-50%, -50%);
  }
  .action--minor { width: 23px; height: 23px; background: #fff; border: 1.6px solid var(--azure); }
  .action--pass { width: 36px; height: 36px; background: #fff; box-shadow: 0 2px 6px rgba(0,0,0,.15); }
  .action--like { width: 36px; height: 36px; background: linear-gradient(135deg, var(--cyan), var(--azure)); }

  .tab-bar {
    position: absolute; left: 0; right: 0; bottom: 0; background: #fff;
  }
  .tab {
    position: absolute; transform: translate(-50%, -50%);
    display: flex; align-items: center; justify-content: center;
  }
  .tab--active-round { width: 25px; height: 25px; border-radius: 50%; background: linear-gradient(135deg, var(--cyan), var(--azure)); }
  .tab--active-square { width: 27px; height: 27px; border-radius: 9px; background: linear-gradient(135deg, var(--cyan), var(--azure)); }

  /* Profile screen */
  .prev-card {
    position: absolute; left: 10px; top: -30px; width: 196px; height: 42px;
    background: var(--card); border-radius: 14px; border-bottom: 1.5px solid var(--cyan);
  }
  .intro-card--about { left: 9px; top: 28px; width: 198px; height: 77px; padding: 18px 10px 0 15px; font-size: 8.2px; line-height: 9.5px; }
  .pill {
    position: absolute; top: 120px; height: 23px; border-radius: 12px;
    display: flex; align-items: center; justify-content: center;
    font-family: "Inter", sans-serif; font-size: 8px; color: #fff;
  }
  .pill--belief { left: 9px; width: 100px; background: var(--cyan); }
  .pill--politics { left: 114px; width: 93px; background: var(--blue); }

  .trait-list {
    position: absolute; left: 9px; top: 157px; width: 198px; height: 194px;
    background: var(--card); border-radius: 14px; border-bottom: 1.5px solid var(--cyan);
    padding: 0 18px 0 14px;
  }
  .trait {
    display: flex; align-items: center; gap: 6px; height: 37px;
    border-bottom: 1px solid var(--line);
  }
  .trait:first-child { margin-top: 6px; }
  .trait:last-child { border-bottom: none; }
  .trait__icon { width: 16px; height: 16px; flex: none; }
  .trait__label { font-size: 8.6px; color: var(--azure); line-height: 11px; }
  .trait__value { font-family: "Inter", sans-serif; font-size: 7.8px; color: #111; line-height: 10px; }

  /* Inbox */
  .inbox-head {
    position: absolute; left: 0; right: 0; top: 0; height: 66px; background: #fff;
  }
  .inbox-head__title {
    position: absolute; left: 0; right: 0; top: 36px; text-align: center;
    font-size: 15px; font-weight: 400; color: #111;
  }
  .thread {
    position: absolute; left: 10px; width: 203px; height: 54px;
    background: #fff; border-radius: 12px;
  }
  .avatar { position: absolute; border-radius: 50%; }
  .thread .avatar { left: 17px; top: 11px; width: 31px; height: 31px; }
  .online { position: absolute; width: 11px; height: 11px; border-radius: 50%; background: var(--online); border: 1.5px solid #fff; }
  .thread .online { left: 12px; top: 33px; }
  .thread__name { position: absolute; left: 56px; top: 15px; font-weight: 800; font-size: 10.5px; line-height: 12px; }
  .thread__text { position: absolute; left: 56px; top: 30px; font-size: 7.8px; color: #222; }
  .thread__time { position: absolute; right: 16px; top: 16px; font-size: 7.8px; color: #8c93a0; display: flex; gap: 2px; align-items: center; }

  /* Chat */
  .chat-head { position: absolute; left: 0; right: 0; top: 0; height: 67px; background: #fff; }
  .chat-head .avatar { left: 40px; top: 34px; width: 25px; height: 25px; }
  .chat-head .online { left: 36px; top: 50px; width: 9px; height: 9px; }
  .chat-head__name { position: absolute; left: 73px; top: 32px; font-weight: 800; font-size: 10.5px; }
  .chat-head__state { position: absolute; left: 73px; top: 48px; font-size: 8px; color: #222; }
  .bubble {
    position: absolute; height: 28px; display: flex; align-items: center; justify-content: center;
    font-size: 9px; color: #fff; border-radius: 10px;
  }
  .bubble--in { left: 14px; top: 81px; width: 179px; background: var(--cyan); border-bottom-left-radius: 0; }
  .bubble--out { left: 136px; top: 213px; width: 76px; background: var(--blue); border-bottom-right-radius: 0; }
  .stamp { position: absolute; font-size: 6.8px; color: #7d8593; }
  .shared-image {
    position: absolute; left: 14px; top: 135px; width: 153px; height: 63px; border-radius: 4px;
    background: radial-gradient(circle at 75% 55%, #e42f2a 0%, transparent 30%),
                linear-gradient(120deg, #f6b21a, #f07a1a 45%, #f7c531 70%, #d9602a);
  }
  .composer {
    position: absolute; left: 9px; top: 267px; width: 203px; height: 34px;
    background: #fff; border: 1px solid #d6deea; border-radius: 17px;
  }
  .composer__placeholder { position: absolute; left: 36px; top: 11px; font-size: 8.8px; color: #9aa1ad; }
  .composer__smile { position: absolute; left: 9px; top: 9px; width: 16px; height: 16px; border-radius: 50%; background: #e4e6ea; }
  .composer__send {
    position: absolute; right: 5px; top: 3px; width: 26px; height: 26px; border-radius: 50%;
    background: linear-gradient(135deg, var(--cyan), var(--blue));
    display: flex; align-items: center; justify-content: center;
  }

  .keyboard {
    position: absolute; left: 0; right: 0; top: 317px; bottom: 0; background: var(--key-bed);
    padding-top: 5px; font-family: "Inter", sans-serif;
  }
  .key-row { display: flex; justify-content: center; gap: 1.2px; margin-bottom: 8px; }
  .key {
    width: 20.9px; height: 24px; background: var(--key); border-radius: 4px;
    display: flex; align-items: center; justify-content: center;
    font-size: 11px; color: #111; box-shadow: 0 1px 0 #8e939c;
  }
  .key-row--home .key { width: 20.9px; }
  .key-row--home { gap: 1.2px; }
  .key--mod { width: 25px; background: var(--key-dark); }
  .key--wide { font-size: 8.5px; }
  .key--num { width: 50px; background: var(--key-dark); }
  .key--space { width: 108px; }
  .key--go { width: 51px; background: var(--key-dark); }
  .keyboard__extras {
    position: absolute; left: 14px; right: 14px; bottom: 8px;
    display: flex; justify-content: space-between;
  }
</style>
</head>
<body>

<svg width="0" height="0" style="position:absolute">
  <defs>
    <symbol id="i-heart" viewBox="0 0 24 24"><path d="M12 21s-8-5.2-8-11.2A4.6 4.6 0 0 1 12 7a4.6 4.6 0 0 1 8 2.8C20 15.8 12 21 12 21z"/></symbol>
    <symbol id="i-heart-line" viewBox="0 0 24 24"><path d="M12 20s-7.5-4.9-7.5-10.5A4.3 4.3 0 0 1 12 7a4.3 4.3 0 0 1 7.5 2.5C19.5 15.1 12 20 12 20z" fill="none" stroke="currentColor" stroke-width="2"/></symbol>
    <symbol id="i-refresh" viewBox="0 0 24 24"><path d="M5 10a7.5 7.5 0 0 1 13.5-2.5M19 14a7.5 7.5 0 0 1-13.5 2.5" fill="none" stroke="currentColor" stroke-width="2.6" stroke-linecap="round"/></symbol>
    <symbol id="i-chat" viewBox="0 0 24 24"><path d="M12 3.5a8.5 8.5 0 0 0-7.4 12.7L3.5 20.5l4.3-1.1A8.5 8.5 0 1 0 12 3.5z" fill="none" stroke="currentColor" stroke-width="1.6"/><circle cx="8.5" cy="12" r="1" fill="currentColor"/><circle cx="12" cy="12" r="1" fill="currentColor"/><circle cx="15.5" cy="12" r="1" fill="currentColor"/></symbol>
    <symbol id="i-sliders" viewBox="0 0 24 24"><g fill="none" stroke="currentColor" stroke-width="1.6" stroke-linecap="round"><path d="M3 6h18M3 12h18M3 18h18"/><circle cx="15" cy="6" r="2" fill="#fff"/><circle cx="8" cy="12" r="2" fill="#fff"/><circle cx="14" cy="18" r="2" fill="#fff"/></g></symbol>
    <symbol id="i-clock" viewBox="0 0 12 12"><circle cx="6" cy="6" r="4.6" fill="none" stroke="currentColor" stroke-width="1"/><path d="M6 3.4V6h2" fill="none" stroke="currentColor" stroke-width="1"/></symbol>
    <symbol id="i-signal" viewBox="0 0 40 10"><g fill="#222"><rect x="0" y="7" width="2" height="3"/><rect x="3.5" y="5" width="2" height="5"/><rect x="7" y="3" width="2" height="7"/><rect x="10.5" y="1" width="2" height="9"/><path d="M19 3.5a6 6 0 0 1 8 0l-1 1a4.6 4.6 0 0 0-6 0zM20.6 5.2a3.6 3.6 0 0 1 4.8 0l-1 1a2.2 2.2 0 0 0-2.8 0zM23 7.2l1 1-1 1-1-1z"/><rect x="30" y="2" width="9" height="6" rx="1.5"/></g></symbol>
  </defs>
</svg>

<header class="brand-mark">
  <span class="brand-mark__name">CORVELLE</span>
  <span class="brand-mark__dot"></span>
</header>

<!-- Daily introduction -->
<section class="screen screen--intro">
  <div class="status"><span>No Signal</span><svg width="40" height="10"><use href="#i-signal"/></svg></div>
  <div class="app-logo"><span class="app-logo__name">CORVELLE</span><span class="app-logo__dot"></span></div>
  <article class="intro-card intro-card--letter">
    <p class="greeting">Dear Darian,</p>
    <p>Allow me to introduce you <strong>Selene</strong> sapien dignissim congue aliquam. Blandit amet nulla tempor erat lectus cras vitae volutpat rhoncus. Sed accumsan tempor enim massa purus. Nec lorem commodo tellus risus cras nisl sit ut. Lorem pharetra pharetra semper facilisi eget. Eget in amet urna massa. Mattis eget viverra massa habitasse non sit volutpat. Lobortis dolor penatibus amet elit.</p>
  </article>
  <div class="photo-frame" role="img" aria-label="Profile photo of the introduced match, smiling on a city street at night"></div>
  <div class="action action--minor" style="left:33px;top:378px"><svg width="11" height="11" viewBox="0 0 10 10"><path d="M1 5h8" stroke="#0a8df0" stroke-width="1.8" stroke-linecap="round"/></svg></div>
  <div class="action action--pass" style="left:79px;top:378px"><svg width="13" height="13" viewBox="0 0 10 10"><path d="M1 1l8 8M9 1L1 9" stroke="#e5262b" stroke-width="1.4" stroke-linecap="round"/></svg></div>
  <div class="action action--like" style="left:134px;top:378px"><svg width="18" height="18" fill="#fff"><use href="#i-heart"/></svg></div>
  <div class="action action--minor" style="left:180px;top:379px"><svg width="11" height="11" viewBox="0 0 10 10"><path d="M1 5h8M5 1v8" stroke="#0a8df0" stroke-width="1.8" stroke-linecap="round"/></svg></div>
  <nav class="tab-bar" style="height:50px">
    <span class="tab" style="left:44px;top:28px;color:#555"><svg width="17" height="17"><use href="#i-refresh"/></svg></span>
    <span class="tab tab--active-round" style="left:89px;top:28px;color:#fff"><svg width="15" height="15"><use href="#i-heart-line"/></svg></span>
    <span class="tab" style="left:134px;top:28px;color:#555"><svg width="18" height="18"><use href="#i-chat"/></svg></span>
    <span class="tab" style="left:169px;top:28px;color:#555"><svg width="19" height="19"><use href="#i-sliders"/></svg></span>
  </nav>
</section>

<!-- Profile details -->
<section class="screen screen--profile">
  <div class="prev-card"></div>
  <article class="intro-card intro-card--about">
    <p>Mus gravida feugiat lobortis aliquet aliquet sapien dignissim congue aliquam. Blandit amet nulla tempor erat lectus cras vitae volutpat rhoncus. Sed accumsan tempor enim massa purus.</p>
  </article>
  <span class="pill pill--belief">Atheis</span>
  <span class="pill pill--politics">Liberal</span>
  <ul class="trait-list">
    <li class="trait">
      <svg class="trait__icon" viewBox="0 0 16 16" fill="#0a8df0"><circle cx="8" cy="2.6" r="2"/><path d="M2 5.5l1-1 3 1.5h4l3-1.5 1 1-3.5 2V15H9v-4H7v4H5.5V7.5z"/></svg>
      <div><div class="trait__label">Children</div><div class="trait__value">Have childern</div></div>
    </li>
    <li class="trait">
      <svg class="trait__icon" viewBox="0 0 16 16" fill="#0a8df0"><circle cx="4" cy="4" r="1.8"/><circle cx="12" cy="4" r="1.8"/><circle cx="8" cy="6.5" r="1.5"/><path d="M1.5 7h5v8h-5zM9.5 7h5v8h-5zM6.5 9h3v5h-3z"/></svg>
      <div><div class="trait__label">Family Goals</div><div class="trait__value">Open to children</div></div>
    </li>
    <li class="trait">
      <svg class="trait__icon" viewBox="0 0 16 16" fill="#0a8df0"><path d="M1 8h14a7 5 0 0 1-14 0z"/><circle cx="5" cy="6" r="2"/><circle cx="9" cy="5.5" r="2.2"/><circle cx="12.5" cy="6.3" r="1.6"/></svg>
      <div><div class="trait__label">Diet</div><div class="trait__value">Omnivore</div></div>
    </li>
    <li class="trait">
      <svg class="trait__icon" viewBox="0 0 16 16" fill="#0a8df0"><path d="M1.5 2h13L9 8.5V13h3v1.5H4V13h3V8.5z"/></svg>
      <div><div class="trait__label">Drinking</div><div class="trait__value">Rarely</div></div>
    </li>
    <li class="trait">
      <svg class="trait__icon" viewBox="0 0 16 16"><rect x="1" y="5" width="14" height="6" rx="3" transform="rotate(40 8 8)" fill="#0a8df0"/><path d="M5.5 4.5l4.6 3.9" stroke="#fff" stroke-width="1.2"/></svg>
      <div><div class="trait__label">Drugs</div><div class="trait__value">Recently</div></div>
    </li>
  </ul>
  <div class="action action--minor" style="left:33px;top:380px"><svg width="11" height="11" viewBox="0 0 10 10"><path d="M1 5h8" stroke="#0a8df0" stroke-width="1.8" stroke-linecap="round"/></svg></div>
  <div class="action action--pass" style="left:79px;top:380px"><svg width="13" height="13" viewBox="0 0 10 10"><path d="M1 1l8 8M9 1L1 9" stroke="#e5262b" stroke-width="1.4" stroke-linecap="round"/></svg></div>
  <div class="action action--like" style="left:135px;top:380px"><svg width="18" height="18" fill="#fff"><use href="#i-heart"/></svg></div>
  <div class="action action--minor" style="left:181px;top:381px"><svg width="11" height="11" viewBox="0 0 10 10"><path d="M1 5h8M5 1v8" stroke="#0a8df0" stroke-width="1.8" stroke-linecap="round"/></svg></div>
  <nav class="tab-bar" style="height:51px">
    <span class="tab" style="left:45px;top:29px;color:#555"><svg width="17" height="17"><use href="#i-refresh"/></svg></span>
    <span class="tab tab--active-round" style="left:90px;top:29px;color:#fff"><svg width="15" height="15"><use href="#i-heart-line"/></svg></span>
    <span class="tab" style="left:135px;top:29px;color:#555"><svg width="18" height="18"><use href="#i-chat"/></svg></span>
    <span class="tab" style="left:170px;top:29px;color:#555"><svg width="19" height="19"><use href="#i-sliders"/></svg></span>
  </nav>
</section>

<!-- Message threads -->
<section class="screen screen--inbox">
  <header class="inbox-head">
    <div class="status"><span>No Signal</span><svg width="40" height="10"><use href="#i-signal"/></svg></div>
    <h1 class="inbox-head__title">Messages</h1>
  </header>

  <div class="thread" style="top:78px">
    <div class="avatar" style="background:#8a7060" role="img" aria-label="Profile photo of Briana"></div>
    <span class="online"></span>
    <div class="thread__name">Briana</div>
    <div class="thread__text">OMG you are stunning</div>
    <div class="thread__time"><svg width="8" height="8"><use href="#i-clock"/></svg>12:38</div>
  </div>
  <div class="thread" style="top:142px">
    <div class="avatar" style="background:#a33a3f" role="img" aria-label="Profile photo of Heleina"></div>
    <div class="thread__name">Heleina</div>
    <div class="thread__text">Oh hi babe!</div>
    <div class="thread__time"><svg width="8" height="8"><use href="#i-clock"/></svg>12:38</div>
  </div>
  <div class="thread" style="top:206px">
    <div class="avatar" style="background:#3d4a3a" role="img" aria-label="Profile photo of Salsa"></div>
    <span class="online"></span>
    <div class="thread__name">Salsa</div>
    <div class="thread__text">Yes, i do!</div>
    <div class="thread__time"><svg width="8" height="8"><use href="#i-clock"/></svg>12:38</div>
  </div>
  <div class="thread" style="top:270px">
    <div class="avatar" style="background:#6b7386" role="img" aria-label="Profile photo of Steven"></div>
    <span class="online"></span>
    <div class="thread__name">Steven</div>
    <div class="thread__text">ur welcome</div>
    <div class="thread__time"><svg width="8" height="8"><use href="#i-clock"/></svg>12:38</div>
  </div>
  <div class="thread" style="top:336px">
    <div class="avatar" style="background:#9b8c80" role="img" aria-label="Profile photo of Salsa"></div>
    <div class="thread__name">Salsa</div>
    <div class="thread__text">Yes, i do!</div>
    <div class="thread__time">12:38</div>
  </div>

  <nav class="tab-bar" style="height:53px">
    <span class="tab" style="left:45px;top:28px;color:#555"><svg width="17" height="17"><use href="#i-refresh"/></svg></span>
    <span class="tab" style="left:92px;top:28px;color:#555"><svg width="19" height="19"><use href="#i-heart-line"/></svg></span>
    <span class="tab tab--active-square" style="left:137px;top:28px;color:#fff"><svg width="17" height="17"><use href="#i-chat"/></svg></span>
    <span class="tab" style="left:175px;top:28px;color:#555"><svg width="19" height="19"><use href="#i-sliders"/></svg></span>
  </nav>
</section>

<!-- Conversation -->
<section class="screen screen--chat">
  <header class="chat-head">
    <div class="status"><span>No Signal</span><svg width="40" height="10"><use href="#i-signal"/></svg></div>
    <svg class="abs" style="left:11px;top:41px" width="15" height="10" viewBox="0 0 15 10"><path d="M14 5H1.5M5.5 1L1.5 5l4 4" fill="none" stroke="#111" stroke-width="1.3"/></svg>
    <div class="avatar" style="background:#7a6a5e" role="img" aria-label="Profile photo of Nico A. Varela"></div>
    <span class="online"></span>
    <div class="chat-head__name">Nico A. Varela</div>
    <div class="chat-head__state">Online</div>
  </header>

  <div class="bubble bubble--in">Hey, Tell me something i don't know</div>
  <span class="stamp" style="left:15px;top:116px">4.30 AM</span>
  <div class="shared-image" role="img" aria-label="Shared image of a crowd of colourful emoji faces"></div>
  <span class="stamp" style="left:15px;top:204px">4.31 AM</span>
  <div class="bubble bubble--out">Awesome</div>
  <span class="stamp" style="right:9px;top:246px">9.30 AM</span>

  <div class="composer">
    <span class="composer__smile"></span>
    <span class="composer__placeholder">Type message...</span>
    <span class="composer__send"><svg width="12" height="8" viewBox="0 0 12 8"><path d="M0.5 4h10M7.5 1l3 3-3 3" fill="none" stroke="#fff" stroke-width="1.2"/></svg></span>
  </div>

  <div class="keyboard">
    <div class="key-row">
      <span class="key">Q</span><span class="key">W</span><span class="key">E</span><span class="key">R</span><span class="key">T</span><span class="key">Y</span><span class="key">U</span><span class="key">I</span><span class="key">O</span><span class="key">P</span>
    </div>
    <div class="key-row key-row--home">
      <span class="key">A</span><span class="key">S</span><span class="key">D</span><span class="key">F</span><span class="key">G</span><span class="key">H</span><span class="key">J</span><span class="key">K</span><span class="key">L</span>
    </div>
    <div class="key-row">
      <span class="key key--mod"><svg width="11" height="11" viewBox="0 0 10 10"><path d="M5 1L1 5.5h2.2V9h3.6V5.5H9z" fill="#111"/></svg></span>
      <span class="key" style="margin-left:3px">Z</span><span class="key">X</span><span class="key">C</span><span class="key">V</span><span class="key">B</span><span class="key">N</span><span class="key">M</span>
      <span class="key key--mod" style="margin-left:3px"><svg width="13" height="9" viewBox="0 0 13 9"><path d="M4 0.5h8.5v8H4L0.5 4.5z" fill="none" stroke="#111" stroke-width="0.9"/><path d="M6.5 2.8l3.4 3.4M9.9 2.8L6.5 6.2" stroke="#111" stroke-width="0.9"/></svg></span>
    </div>
    <div class="key-row">
      <span class="key key--num key--wide">123</span>
      <span class="key key--space key--wide">space</span>
      <span class="key key--go key--wide">Go</span>
    </div>
    <div class="keyboard__extras">
      <svg width="16" height="16" viewBox="0 0 16 16"><circle cx="8" cy="8" r="7" fill="none" stroke="#555" stroke-width="1.1"/><circle cx="5.6" cy="6.3" r="0.9" fill="#555"/><circle cx="10.4" cy="6.3" r="0.9" fill="#555"/><path d="M4.6 9.5a3.6 3.6 0 0 0 6.8 0" fill="none" stroke="#555" stroke-width="1.1"/></svg>
      <svg width="12" height="16" viewBox="0 0 12 16"><rect x="3.5" y="1" width="5" height="9" rx="2.5" fill="none" stroke="#555" stroke-width="1.1"/><path d="M1.5 7.5a4.5 4.5 0 0 0 9 0M6 12v3" fill="none" stroke="#555" stroke-width="1.1"/></svg>
    </div>
  </div>
</section>

</body>
</html>
```